Product Page

We're marketing an on line educational product, and need a savvy designer to fix a web page that lacks pazazz. We're looking for a designer who can take a lot of information and present it neatly and elegantly, and put all the relevant testimonials in there without loosing cool factor. Right now we need just one page designed, but the winner will have the chance to re-do the entire site, with lots more content coming down the line that will need the new look.

The current page is here: www.plorvetune.com/sign-up. This should be combined with the attached PDF that has a lot more text information.

Note: The previous file listed as a pdf was a jpg. Sorry about that! Now there's a real pdf available for you to download.

I have added a jpg of myself. If you can use that I would appreciate it. I've also uploaded an example of a pricing page. Let me know how you would charge for this extra page.

Target Market(s)

Men and women in their forties who want to improve their singing but have other careers and are looking for high quality voice instruction.

The page must have an attractive "Get Started" button prominently displayed.

Industry/Entity Type

Marketing

Requirements
Must have
• Above the fold: clear buy now button, some testimonials, and the video. Should have a background that makes reading the text easy-not black. The new page must work somehow with the existing theme, although we will be re-designing the whole site soon with your help.
Nice to have
• Some navigation to organize a lot of text

```html
<!DOCTYPE html>
<html lang="en">
<head>
<meta charset="utf-8">
<title>Marden School of Voice – Vocal Ascent</title>
<link rel="stylesheet" href="https://fonts.googleapis.com/css2?family=Cabin:wght@400;500;700&family=Open+Sans:ital,wght@0,400;0,600;1,700&family=Carlito:wght@400;700&display=swap">
<style>
  :root {
    --brand-blue: #1ea6dc;
    --link-blue: #2191cf;
    --sign-orange: #f39a12;
    --text-dark: #444;
    --text-body: #333;
    --text-muted: #9a9a9a;
    --logo-gray: #8a8a8a;
    --rule: #d4d4d4;
    --hero-dark: #4b4d5b;
    --hero-mid: #8d8f98;
    --hero-light: #b9bbc1;
    --white: #ffffff;
  }
  * { box-sizing: border-box; margin: 0; padding: 0; }
  html, body { width: 1064px; height: 1200px; overflow: hidden; background: var(--white); }
  body { position: relative; font-family: "Open Sans", sans-serif; color: var(--text-body); }

  /* Header */
  .site-header { position: absolute; left: 0; top: 0; width: 1064px; height: 114px; border-bottom: 1px solid var(--rule); }
  .brand { position: absolute; left: 30px; top: 36px; display: flex; align-items: center; gap: 12px; }
  .brand-mark { width: 28px; height: 28px; background: var(--brand-blue); }
  .brand-name { font-family: "Cabin", sans-serif; font-weight: 500; color: var(--logo-gray); font-size: 22px; line-height: 1; }
  .sign-in { position: absolute; left: 953px; top: 33px; width: 71px; height: 27px; background: var(--sign-orange); color: var(--white);
    font-family: "Carlito", sans-serif; font-weight: 700; font-size: 13.5px; display: flex; align-items: center; justify-content: center; text-decoration: none; }
  .main-nav { position: absolute; right: 34px; top: 79px; display: flex; font-family: "Cabin", sans-serif; font-size: 13.5px; color: var(--text-dark); }
  .main-nav a { color: inherit; text-decoration: none; }
  .main-nav a + a::before { content: "I"; margin: 0 12px; font-size: 11px; color: var(--text-dark); }

  /* Hero */
  .hero { position: absolute; left: 0; top: 115px; width: 1064px; height: 422px;
    background: linear-gradient(100deg, var(--hero-dark) 0%, var(--hero-mid) 45%, var(--hero-light) 70%, var(--hero-mid) 100%); }
  .hero-photo { position: absolute; right: 0; top: 0; width: 400px; height: 422px;
    background: radial-gradient(ellipse at 55% 55%, #c9a393 0%, #7d6a66 40%, rgba(90,92,104,0) 75%); }
  .hero-title { position: absolute; left: 68px; top: 104px; font-family: "Cabin", sans-serif; font-size: 26px; line-height: 35px; color: var(--white); }
  .hero-title strong { font-family: "Open Sans", sans-serif; font-weight: 600; font-size: 24px; }
  .play-button { position: absolute; left: 574px; top: 141px; width: 66px; height: 43px; background: #3a3a3c; border: 1px solid #5a5a5a;
    display: flex; align-items: center; justify-content: center; }
  .hero-copy { position: absolute; left: 68px; top: 256px; width: 420px; font-size: 15.5px; line-height: 23px; color: #d7d8dc; }
  .buy-now { position: absolute; left: 497px; top: 267px; width: 142px; height: 48px; background: var(--brand-blue); color: var(--white);
    font-family: "Carlito", sans-serif; font-weight: 700; font-size: 24px; display: flex; align-items: center; justify-content: center; text-decoration: none;
    box-shadow: 0 1px 3px rgba(0,0,0,.3); }

  /* Intro */
  .intro { position: absolute; left: 62px; top: 578px; width: 960px; font-family: "Cabin", sans-serif; font-size: 27px; line-height: 36px; color: var(--text-dark); }
  .intro a { color: var(--link-blue); text-decoration: none; }

  /* Community grid */
  .vocalist-grid { position: absolute; left: 64px; top: 696px; width: 450px; height: 450px;
    background: linear-gradient(135deg, #3a3a3a 0%, #8c8c8c 35%, #2c2c2c 60%, #a8a8a8 100%); }

  /* Testimonials */
  .testimonial { position: absolute; left: 551px; width: 470px; }
  .testimonial-one { top: 692px; }
  .testimonial-two { top: 912px; }
  .quote-open, .quote-close { position: absolute; }
  .quote-open { left: 0; top: 0; }
  .quote-body { margin-left: 38px; padding-top: 12px; font-size: 12.6px; line-height: 18px; color: var(--text-body); width: 415px; }
  .quote-close { left: 433px; }
  .author { margin-left: 38px; margin-top: 26px; font-size: 10.5px; line-height: 15px; font-style: italic; font-weight: 700; color: var(--text-muted); }
</style>
</head>
<body>
  <header class="site-header">
    <div class="brand">
      <span class="brand-mark"></span>
      <span class="brand-name">Marden School of Voice</span>
    </div>
    <a class="sign-in" href="#">SIGN IN</a>
    <nav class="main-nav">
      <a href="#">Home</a>
      <a href="#">Voice Lessons</a>
      <a href="#">Blog</a>
      <a href="#">What Students Say</a>
      <a href="#">Meet the Instrutors</a>
      <a href="#">Vocal Ascent</a>
    </nav>
  </header>

  <section class="hero">
    <div class="hero-photo" role="img" aria-label="Photo of a woman singing joyfully while wearing headphones"></div>
    <h1 class="hero-title">It’s the difference between polishing a pretty stone,<br>and digging a little deeper, to <strong>strike gold.</strong></h1>
    <a class="play-button" href="#" aria-label="Play video">
      <svg width="18" height="20" viewBox="0 0 18 20"><path d="M1 1 L17 10 L1 19 Z" fill="#d8d8d8"/></svg>
    </a>
    <p class="hero-copy">Many voice teachers promose to help your singing. The Vocal Ascent programs is uniquely positioned to transform the way your voice works.</p>
    <a class="buy-now" href="#">BUY NOW</a>
  </section>

  <h2 class="intro">If you’re ready to see what your voice can do, check out <a href="#">Vocal Ascent</a><br>and join the growing, worldwide network of vocalists.</h2>

  <div class="vocalist-grid" role="img" aria-label="Black and white grid of sixteen photos of singers performing with microphones"></div>

  <blockquote class="testimonial testimonial-one">
    <svg class="quote-open" width="30" height="22" viewBox="0 0 30 22"><path d="M2 22 V12 Q2 3 11 1 L12 4 Q7 6 7 10 H12 V22 Z M17 22 V12 Q17 3 26 1 L27 4 Q22 6 22 10 H27 V22 Z" fill="var(--brand-blue)"/></svg>
    <p class="quote-body">Since starting the program, my singing progres has been described as phenomenal, 400% improvement. My teachers have worked with people such as Dame Ilse Varrow, and they are impressed with my voice. I still feel I have progress to make, but mainly in areas of classical style. The raw instrument is there now....</p>
    <svg class="quote-close" style="top:93px" width="30" height="22" viewBox="0 0 30 22"><path d="M28 0 V10 Q28 19 19 21 L18 18 Q23 16 23 12 H18 V0 Z M13 0 V10 Q13 19 4 21 L3 18 Q8 16 8 12 H3 V0 Z" fill="var(--brand-blue)"/></svg>
    <p class="author">Owen Pritchard<br>Australia</p>
  </blockquote>

  <blockquote class="testimonial testimonial-two">
    <svg class="quote-open" width="30" height="22" viewBox="0 0 30 22"><path d="M2 22 V12 Q2 3 11 1 L12 4 Q7 6 7 10 H12 V22 Z M17 22 V12 Q17 3 26 1 L27 4 Q22 6 22 10 H27 V22 Z" fill="var(--brand-blue)"/></svg>
    <p class="quote-body">I have found through the years that the one method I can count on is Vocal Ascent. Elias Marden has put together the fool proof method for training a voice that is dependable and authentic as you grow through your vocal practice. I recently joined a band with a harder rock sound than I had been used to. I worked through Vocal Ascent front to back, and now I am killing it on songs I had previously only dreamed about....</p>
    <svg class="quote-close" style="top:126px" width="30" height="22" viewBox="0 0 30 22"><path d="M28 0 V10 Q28 19 19 21 L18 18 Q23 16 23 12 H18 V0 Z M13 0 V10 Q13 19 4 21 L3 18 Q8 16 8 12 H3 V0 Z" fill="var(--brand-blue)"/></svg>
    <p class="author">Carla Wendt<br>San Francisco</p>
  </blockquote>
</body>
</html>
```